Web Design Project for an operational risk management consulting company

Website is for a consulting company specialising in operational risk management. Our specialist areas include crisis and emergency management, community engagement, safety and security. We work internationally, generally in high hazard environments. We are a highly ethical and professional company which prides itself on delivering a strong level of customer service.

As a company we recognise that the key to keeping people safe is ensuring that they work in an ethical and sustainable manner. Therefore we are as much about soft skills as we are about hard skills. We would like our website and supporting images to reflect this.
We have worked throughout Africa and the Middle east, as well as Asia pacific. An international flavour to the website would also be great.
Background images on www.corvellpartnersglobal.example are a good example of what we are thinking of, though very open to fresh ideas.

Target Market(s)

Our customers are generally medium to large organisations who work internationally. We would like to also support more not for profits and non government organisations who work in hazardous environments

Industry/Entity Type

It Company

Number of Pages Required

5+ page

Font styles to use
Sans Serif

Requirements
Must have
• Easy to edit by non IT people
• Section for blogs/news updates
• Pages should include:
• (A) home page
• (B) about us
• (C) services
• (D) contact
• (E) insights
Nice to have
• An international and professional theme. Some gritty images that symbolise the risks associated with working in unstable environments, as well as some human ones and that of the environment
Should not have
• Cartoonish or generic images
• Not focus on traditional physical security aspects

```html
<!DOCTYPE html>
<html lang="en">
<head>
<meta charset="utf-8">
<title>Corvell Risk — Operational Risk Management</title>
<link href="https://fonts.googleapis.com/css2?family=Open+Sans:wght@400;600;700;800&display=swap" rel="stylesheet">
<style>
:root{
  --navy:#0b4d72;
  --navy-dark:#073a57;
  --navy-deep:#052c43;
  --accent:#1b7fb8;
  --ink:#2f3a42;
  --muted:#7b858c;
  --line:#e3e6e8;
  --white:#ffffff;
  --page:#ffffff;
}
*{box-sizing:border-box;margin:0;padding:0}
html,body{width:1200px;height:2316px;overflow:hidden}
body{position:relative;background:var(--page);font-family:"Open Sans",Arial,sans-serif;color:var(--ink)}
.abs{position:absolute}

/* header */
.site-header{left:0;top:0;width:1200px;height:88px;background:var(--white);box-shadow:0 1px 4px rgba(0,0,0,.08);z-index:2}
.brand{left:118px;top:16px;display:flex;flex-direction:column;align-items:center;gap:4px}
.brand-mark{width:38px;height:38px;border-radius:50%;background:var(--navy)}
.brand-name{font-size:13px;font-weight:700;color:var(--navy)}
.main-nav{right:78px;top:36px;display:flex;gap:34px}
.main-nav a{font-size:11px;font-weight:600;color:#5d6870;text-decoration:none;letter-spacing:.5px;padding-bottom:8px}
.main-nav a.active{color:var(--navy);border-bottom:2px solid var(--navy)}

/* hero */
.hero{left:0;top:88px;width:1200px;height:572px;background:linear-gradient(180deg,#cfd6da 0%,#b7c0c6 45%,#8e979e 72%,#5f686f 100%)}
.hero-text{left:58px;top:140px;width:430px}
.hero-title{font-size:46px;font-weight:800;color:#1f2b33;letter-spacing:1px;line-height:1}
.hero-sub{font-size:30px;font-weight:400;color:#1f2b33;margin-top:8px}
.hero-copy{font-size:12px;line-height:18px;color:#2f3a42;margin-top:14px}
.hero-arrow{top:278px;width:26px;height:26px;border-radius:50%;background:rgba(255,255,255,.55);display:flex;align-items:center;justify-content:center}

/* welcome */
.welcome{left:0;top:660px;width:1200px;height:300px;text-align:center}
.welcome h1{margin-top:60px;font-size:30px;font-weight:400;color:#3a454c;letter-spacing:1px}
.welcome h1 span{color:var(--navy)}
.welcome p{width:820px;margin:22px auto 0;font-size:12px;line-height:19px;color:var(--muted)}
.btn{display:inline-block;background:var(--navy);color:var(--white);font-size:10px;font-weight:700;letter-spacing:1px;padding:10px 26px;border-radius:2px}
.welcome .btn{margin-top:24px}

/* services */
.services{left:0;top:960px;width:1200px;height:570px;background:linear-gradient(180deg,#2d3a2c 0%,#4c5f3c 35%,#6f8a4a 60%,#3e5a2a 100%)}
.services-head{top:58px;width:1200px;text-align:center;color:var(--white)}
.services-head h2{font-size:36px;font-weight:400}
.services-head p{width:640px;margin:10px auto 0;font-size:11px;line-height:17px;color:#e6ece2}
.service-card{top:200px;width:232px;height:310px;background:var(--white);padding:8px;box-shadow:0 2px 8px rgba(0,0,0,.25);text-align:center}
.service-img{width:216px;height:160px}
.service-card h3{font-size:13px;font-weight:600;color:#3a454c;margin-top:18px}
.service-card p{font-size:10.5px;line-height:16px;color:var(--muted);margin-top:10px;padding:0 14px}

/* risk + news */
.section-title{font-size:20px;font-weight:600;color:#3a454c}
.risk{left:100px;top:1590px;width:400px}
.risk-img{width:360px;height:186px;margin-top:24px;background:linear-gradient(135deg,#2c5f93 0%,#5a87b4 45%,#c6d3df 100%)}
.risk h4{font-size:11.5px;font-weight:600;color:#3a454c;margin-top:14px}
.risk p{font-size:10.5px;line-height:16px;color:var(--muted);margin-top:6px;width:360px}
.news{left:564px;top:1590px;width:540px}
.news-item{display:flex;gap:56px;margin-top:24px}
.news-item + .news-item{margin-top:48px}
.news-thumb{width:100px;height:76px;flex:none}
.news-body h4{font-size:12px;font-weight:600;color:#3a454c}
.news-date{font-size:10px;font-weight:600;color:var(--accent);margin-top:8px}
.news-body p{font-size:10.5px;line-height:16px;color:var(--muted);margin-top:6px;width:360px}

/* footer */
.site-footer{left:0;top:2020px;width:1200px;height:250px;background:var(--navy)}
.footer-brand{left:176px;top:60px;display:flex;flex-direction:column;align-items:center;gap:10px}
.footer-brand .brand-mark{width:56px;height:56px;background:var(--white)}
.footer-brand .brand-name{color:var(--white);font-size:15px}
.footer-col{top:46px;color:#d5e2ea}
.footer-col h5{font-size:11px;font-weight:700;color:var(--white);letter-spacing:.5px;margin-bottom:14px}
.footer-col li{list-style:none;font-size:10.5px;line-height:18px}
.footer-col p{font-size:10.5px;line-height:16px}
.signup-form{display:flex;margin-top:16px}
.signup-input{width:170px;height:30px;background:var(--white);font-size:10px;color:#999;padding:8px 8px}
.signup-btn{height:30px;padding:9px 12px;font-size:10px;font-weight:700;color:var(--white);border:1px solid #d5e2ea;margin-left:4px}
.contact-line{display:flex;align-items:center;gap:8px;font-size:10.5px;line-height:18px}
.footer-bar{left:0;top:2270px;width:1200px;height:46px;background:var(--navy-deep);text-align:center;font-size:10px;color:#a8bccb;padding-top:16px}
.to-top{right:36px;top:14px;width:20px;height:20px;border:1px solid #5f7f94;display:flex;align-items:center;justify-content:center}
</style>
</head>
<body>

<header class="site-header abs">
  <div class="brand abs">
    <span class="brand-mark"></span>
    <span class="brand-name">Corvell Risk</span>
  </div>
  <nav class="main-nav abs">
    <a class="active">HOME</a>
    <a>ABOUT US</a>
    <a>OUR SERVICES</a>
    <a>INSIGHTS</a>
    <a>CONTACT US</a>
  </nav>
</header>

<section class="hero abs" role="img" aria-label="City skyline with people hanging from and balancing heavy concrete blocks, symbolising operational risk">
  <div class="hero-text abs">
    <div class="hero-title">OPERATIONAL</div>
    <div class="hero-sub">Risk Management</div>
    <p class="hero-copy">Lorem ipsum dolor sit amet, consectetur adipiscing elit, sed do eiusmod tempor incididunt ut labore et dolore magna aliqua.</p>
  </div>
  <div class="hero-arrow abs" style="left:14px">
    <svg width="10" height="10" viewBox="0 0 10 10"><path d="M7 1 3 5l4 4" fill="none" stroke="#333" stroke-width="1.6"/></svg>
  </div>
  <div class="hero-arrow abs" style="right:14px">
    <svg width="10" height="10" viewBox="0 0 10 10"><path d="M3 1l4 4-4 4" fill="none" stroke="#333" stroke-width="1.6"/></svg>
  </div>
</section>

<section class="welcome abs">
  <h1>WELCOME TO <span>CORVELL RISK</span></h1>
  <p>Lorem ipsum dolor sit amet, consectetur adipiscing elit, sed do eiusmod tempor incididunt ut labore et dolore magna aliqua. Ut enim ad minim veniam, quis nostrud exercitation ullamco laboris nisi ut aliquip ex ea commodo consequat. Duis aute irure dolor in reprehenderit in voluptate velit esse cillum dolore eu fugiat nulla pariatur. Excepteur sint occaecat cupidatat non proident.</p>
  <span class="btn">LEARN MORE</span>
</section>

<section class="services abs" role="img" aria-label="Green grass field under a dark sky">
  <div class="services-head abs">
    <h2>Our Services</h2>
    <p>Lorem ipsum dolor sit amet, consectetur adipiscing elit, sed do eiusmod tempor incididunt ut labore et dolore magna aliqua. Ut enim ad minim veniam, quis nostrud exercitation.</p>
  </div>

  <article class="service-card abs" style="left:100px">
    <div class="service-img" role="img" aria-label="Business team meeting around a table" style="background:linear-gradient(135deg,#c9cbc8,#6d7478)"></div>
    <h3>Emergency Management</h3>
    <p>Lorem ipsum dolor sit amet, consec adipisc elit, sed do eiusmod.</p>
  </article>
  <article class="service-card abs" style="left:360px">
    <div class="service-img" role="img" aria-label="Hands holding a seedling in soil" style="background:linear-gradient(135deg,#9a6a47,#4c3423)"></div>
    <h3>Community Engagement</h3>
    <p>Lorem ipsum dolor sit amet, consec adipisc elit, sed do eiusmod.</p>
  </article>
  <article class="service-card abs" style="left:620px">
    <div class="service-img" role="img" aria-label="Digital security padlock on a blue screen" style="background:linear-gradient(135deg,#2a6fa5,#0d2f52)"></div>
    <h3>Safety and Security</h3>
    <p>Lorem ipsum dolor sit amet, consec adipisc elit, sed do eiusmod.</p>
  </article>
  <article class="service-card abs" style="left:880px">
    <div class="service-img" role="img" aria-label="International team working together" style="background:linear-gradient(135deg,#b9cbd6,#5f8197)"></div>
    <h3>We work Internationally</h3>
    <p>Lorem ipsum dolor sit amet, consec adipisc elit, sed do eiusmod.</p>
  </article>
</section>

<section class="risk abs">
  <h2 class="section-title">Risk Management</h2>
  <div class="risk-img" role="img" aria-label="Businessman working at a desk with charts"></div>
  <h4>Nemo enim ipsum voluptatem</h4>
  <p>Lorem ipsum dolor sit amet, consectetur adipiscing elit, sed do eiusmod tempor incididunt ut labore et dolore magna aliqua enim ad minim veniam.</p>
</section>

<section class="news abs">
  <h2 class="section-title">News Release</h2>
  <article class="news-item">
    <div class="news-thumb" role="img" aria-label="Person writing notes at a laptop" style="background:linear-gradient(135deg,#d9dde0,#8c969d)"></div>
    <div class="news-body">
      <h4>Nemo enim ipsum voluptatem</h4>
      <div class="news-date">APRIL 10, 2015</div>
      <p>Lorem ipsum dolor sit amet, consectetur adipiscing elit, sed do eiusmod tempor incididunt ut labore et dolore magna aliqua.</p>
    </div>
  </article>
  <article class="news-item">
    <div class="news-thumb" role="img" aria-label="Magnifying glass over documents" style="background:linear-gradient(135deg,#3c4d5c,#101a24)"></div>
    <div class="news-body">
      <h4>Nemo enim ipsum voluptatem</h4>
      <div class="news-date">APRIL 10, 2015</div>
      <p>Lorem ipsum dolor sit amet, consectetur adipiscing elit, sed do eiusmod tempor incididunt ut labore et dolore magna aliqua.</p>
    </div>
  </article>
</section>

<footer class="site-footer abs">
  <div class="footer-brand abs">
    <span class="brand-mark"></span>
    <span class="brand-name">Corvell Risk</span>
  </div>
  <div class="footer-col abs" style="left:400px">
    <h5>INFORMATION</h5>
    <ul>
      <li>Home</li><li>About Us</li><li>Our Services</li><li>Insights</li><li>Contact Us</li>
    </ul>
  </div>
  <div class="footer-col abs" style="left:580px;width:280px">
    <h5>SIGN UP FOR NEWSLETTER</h5>
    <p>Lorem ipsum dolor sit amet, consectetur adipiscing elit sed do eiusmod tempor incididunt.</p>
    <div class="signup-form">
      <span class="signup-input">Enter Email</span>
      <span class="signup-btn">SUBSCRIBE</span>
    </div>
  </div>
  <div class="footer-col abs" style="left:935px">
    <h5>CONTACT US</h5>
    <p>Corvell Risk<br>PO Box 1042, Northgate</p>
    <div class="contact-line" style="margin-top:12px">
      <svg width="11" height="11" viewBox="0 0 12 12"><path d="M2.5 1h2l1 3-1.3 1a7 7 0 0 0 3 3l1-1.3 3 1v2c0 .6-.4 1-1 1A10 10 0 0 1 1.5 2c0-.6.4-1 1-1z" fill="#d5e2ea"/></svg>
      +1 (555) 010 0142
    </div>
    <div class="contact-line">
      <svg width="11" height="11" viewBox="0 0 12 12"><rect x="1" y="2.5" width="10" height="7" fill="none" stroke="#d5e2ea"/><path d="M1 2.5l5 4 5-4" fill="none" stroke="#d5e2ea"/></svg>
      info@corvellrisk.example
    </div>
  </div>
</footer>

<div class="footer-bar abs">
  © 2015 - 2016 Corvell Risk. All Rights Reserved.
  <span class="to-top abs">
    <svg width="10" height="10" viewBox="0 0 10 10"><path d="M1 7l4-4 4 4" fill="none" stroke="#a8bccb" stroke-width="1.4"/></svg>
  </span>
</div>

</body>
</html>
```